BRIGHTDESK - Remote Tech Support Site

We are looking for a new very responsive and simple website for our brand Brightdesk.com - a remote technical support company.

This company supports customers Globally in different countries throughout Eur/ North America / South America / Asia etc (please keep this in mind and integrate into the idea).

Its important to us that the design is very explanatory, the customer should easily be able to figure out that we provide computer support right away ... I like one page responsive type designs as well without a bunch of menu items

Here are some similar sites we like - but still looking for a unique design that fits out brand "brightdesk" - I have upload also some layouts i like (but the designs are not important just the layouts), youll see it includes consumer business etc which is important.

VOLM.COM - I love how clean it is - nice and white easy to see everything

PLUMWIRE247.COM - also nice the layout and responsive one page design makes it easy to use

corvalfix.com - similar to plumwire design as well - you can get the idea im looking for between the two

You will notice those examples are much different then the attachments I added - again this is more of an idea for possible layouts .. attached is also the logo - could inspire color scheme / blue white black etc

Target Market(s)

Home consumers without computer knowledge , older age 45-65, small medium business ... computer repair - slow computers

Industry/Entity Type

Computer Repair

Logo Text

Brightdesk

Coding

Coded - Design and coding required

Number of Pages Required

1 page

Font styles to use
Sans Serif
Other font styles liked:
• your choice responsive

Colors

Designer to choose colors to be used in the design.

Requirements
Must have
• Clean - responsive - professional design - the name says it all - brightdesk
• CALL TO ACTIONS FOR "Get Help Now!" / "Learn More" etc
Nice to have
• We are looking for a new very responsive and simple website for our brand Brightdesk.com - a remote technical support company.
• This company supports customers Globally in different countries throughout Eur/ North America / South America / Asia etc (please keep this in mind and integrate into the idea).
• Its important to us that the design is very explanatory, the customer should easily be able to figure out that we provide computer support right away ... I like one page responsive type designs as well without a bunch of menu items
• Here are some similar sites we like - but still looking for a unique design that fits out brand "brightdesk" - I have upload also some layouts i like (but the designs are not important just the layouts), youll see it includes consumer business etc which is important.
• VOLM.COM - I love how clean it is - nice and white easy to see everything
• PLUMWIRE247.COM - also nice the layout and responsive one page design makes it easy to use
• corvalfix.com - similar to plumwire design as well - you can get the idea im looking for between the two
Should not have
• dark, packed page - bad small font -

```html
<!DOCTYPE html>
<html lang="en">
<head>
<meta charset="utf-8">
<title>Brightdesk – Remote Tech Support</title>
<link href="https://fonts.googleapis.com/css2?family=Lato:wght@300;400;700;900&family=PT+Sans:wght@400;700&display=swap" rel="stylesheet">
<style>
:root{
  --blue:#1e8ff0;
  --blue-dark:#1773c7;
  --blue-pale:#eaf3fd;
  --ink:#1a1a1a;
  --text:#555;
  --muted:#888;
  --line:#dcdcdc;
  --white:#fff;
}
*{box-sizing:border-box;margin:0;padding:0}
h1,h2,h3{font-weight:400}
html,body{width:1200px;height:3186px;overflow:hidden}
body{position:relative;background:var(--white);font-family:"PT Sans",Arial,sans-serif;color:var(--text)}
.abs{position:absolute}
.btn{position:absolute;background:var(--blue);color:var(--white);font-family:"PT Sans",Arial,sans-serif;font-size:18px;display:flex;align-items:center;justify-content:center}

/* header + hero */
.hero{left:0;top:0;width:1200px;height:680px;background:linear-gradient(100deg,#f4f2ee 0%,#ebe7e0 45%,#d9d2c8 70%,#c8c0b6 100%)}
.site-header{left:0;top:0;width:1200px;height:85px;background:rgba(255,255,255,.85)}
.brand{display:flex;align-items:center;gap:8px;font-family:"Lato",sans-serif;font-weight:700;color:var(--blue)}
.brand .dot{border-radius:50%;background:var(--blue)}
.site-header .brand{left:78px;top:14px;font-size:40px}
.site-header .brand .dot{width:50px;height:50px}
.nav{right:78px;top:33px;display:flex;gap:66px;font-family:"Lato",sans-serif;font-size:14px;letter-spacing:1px;color:#777}
.nav .active{color:var(--ink)}
.hero-eyebrow{left:80px;top:214px;font-family:"Lato",sans-serif;font-weight:900;font-size:29px;color:var(--blue)}
.hero-title{left:80px;top:246px;font-family:"Lato",sans-serif;font-weight:900;font-size:42px;color:var(--ink)}
.hero-lead{left:80px;top:306px;width:460px;font-size:17px;line-height:22px;color:#444}
.hero-rule{left:80px;top:384px;width:475px;height:2px;background:var(--blue)}
.subscribe-label{left:80px;top:414px;font-size:21px;color:#333}
.email-field{left:80px;top:454px;width:268px;height:48px;border:2px solid #555;background:var(--white);font-size:14px;color:#777;padding:14px 12px}
.slide-arrow{top:558px;width:46px;height:46px;color:var(--white);display:flex;align-items:center;justify-content:center;font-size:20px;font-weight:700}

/* how it works / member */
.works{left:0;top:680px;width:598px;height:570px;background:linear-gradient(135deg,#202020,#2b2b2b 60%,#1a1a1a)}
.member{left:598px;top:680px;width:602px;height:570px;background:linear-gradient(135deg,#4a4a4a,#3b3b3b 60%,#303030)}
.section-dark-title{font-family:"Lato",sans-serif;font-weight:300;font-size:33px;color:var(--white);letter-spacing:.5px}
.step-title{font-family:"PT Sans",sans-serif;font-weight:700;font-size:19px;color:var(--blue)}
.step-text{font-size:14px;line-height:19px;color:#eee}
.price{color:var(--white)}
.divider-diamond{left:576px;top:656px;width:46px;height:46px;transform:rotate(45deg);background:var(--white);border:5px solid var(--blue)}

/* about */
.about-title{left:528px;top:1298px;font-family:"Lato",sans-serif;font-weight:300;font-size:36px;color:var(--blue)}
.about-text{left:80px;width:680px;font-size:14.5px;line-height:26px;color:#666}
.monitor{left:786px;top:1300px;width:336px;height:292px;background:linear-gradient(180deg,#1a1a1a 0%,#2a2a2a 72%,#c9c9c9 76%,#e6e6e6 100%)}
.quote-band{left:543px;top:1634px;width:657px;height:418px;background:var(--blue-pale)}
.about-photo{left:78px;top:1584px;width:596px;height:416px;background:linear-gradient(135deg,#d8d4cc,#b9afa3 55%,#6e655c)}
.quote-mark{left:728px;top:1705px;font-family:Georgia,serif;font-size:70px;color:#c9cfd6;line-height:1}
.quote-text{left:776px;top:1736px;width:352px;font-size:13.5px;line-height:23px;color:#555}
.quote-name{left:784px;top:1870px;font-size:18px;color:var(--blue)}
.quote-place{left:784px;top:1902px;font-size:15px;color:#333}
.dots{left:932px;top:1948px;display:flex;gap:10px}
.dots span{width:10px;height:10px;border-radius:50%;border:1.5px solid var(--blue-dark)}
.dots span.on{background:var(--blue-dark)}

/* features */
.features-title{left:0;top:2096px;width:1200px;text-align:center;font-family:"Lato",sans-serif;font-weight:300;font-size:34px;color:var(--blue)}
.features{left:77px;top:2163px;display:flex;gap:8px}
.feature{position:relative;width:203px;height:302px;border:1px solid var(--line);background:var(--white)}
.feature.active{background:#f2f2f2;border-color:#eee;box-shadow:0 6px 14px rgba(0,0,0,.25)}
.feature-ring{position:absolute;left:16px;top:30px;width:170px;height:170px;border-radius:50%;border:7px solid #b6d9f8;display:flex;align-items:center;justify-content:center}
.feature-ring .inner{width:142px;height:142px;border-radius:50%;border:2px solid #333;display:flex;align-items:center;justify-content:center;background:var(--white)}
.feature.active .feature-ring{border-color:#666}
.feature-name{position:absolute;left:0;top:222px;width:100%;text-align:center;font-size:16px;color:#333}
.feature.active .feature-name{color:var(--blue)}
.feature-more{position:absolute;left:0;top:250px;width:100%;text-align:center;font-size:13px;color:#333;text-decoration:underline}

/* help band */
.help{left:0;top:2518px;width:1200px;height:272px;background:linear-gradient(90deg,#f5f8fb,#e6edf3 55%,#c9d3dc)}
.help-title{left:0;top:2566px;width:1200px;text-align:center;font-family:"Lato",sans-serif;font-weight:300;font-size:34px;color:var(--blue)}
.help-text{left:240px;top:2620px;width:720px;text-align:center;font-size:13.5px;line-height:26px;color:#777}
.help-btn{top:2682px;height:48px}

/* footer */
.footer{left:0;top:2790px;width:1200px;height:343px;background:linear-gradient(135deg,#2a2520,#3d352d 50%,#26221e)}
.footer-head{font-family:"Lato",sans-serif;font-weight:400;font-size:21px;color:var(--white)}
.footer-list{list-style:none;font-size:14px;line-height:25px;color:var(--white)}
.footer-list li::before{content:"› ";color:#aaa}
.footer-text{font-size:14.5px;line-height:22px;color:var(--white)}
.footer-brand{left:910px;top:2836px;font-size:33px}
.social{width:48px;height:48px;border-radius:50%;border:3px solid var(--white)}
.copyright{left:0;top:3133px;width:1200px;height:53px;background:var(--blue);color:var(--white);font-size:14px;display:flex;align-items:center;justify-content:center}
</style>
</head>
<body>

<!-- Hero -->
<section class="hero abs" role="img" aria-label="Smiling woman relaxing on a white sofa with a laptop in a bright living room"></section>
<header class="site-header abs">
  <div class="brand abs"><span class="dot"></span>brightdesk</div>
  <nav class="nav abs"><span class="active">HOME</span><span>ABOUT US</span><span>SERVICES</span><span>FAQ</span><span>CONTACT US</span></nav>
</header>
<div class="hero-eyebrow abs">DEDICATED SUPPORT</div>
<h1 class="hero-title abs">ANYTIME... ANYWHERE</h1>
<p class="hero-lead abs">The best source out there, we have everything for your computer and internet security!</p>
<div class="hero-rule abs"></div>
<div class="subscribe-label abs">Subscribe Here For Data release and Update</div>
<div class="email-field abs">Email id</div>
<div class="btn" style="left:355px;top:454px;width:145px;height:48px">Submit</div>
<div class="slide-arrow abs" style="left:78px;background:#9a9a9a">«</div>
<div class="slide-arrow abs" style="left:130px;background:var(--blue)">»</div>

<!-- How it works -->
<section class="works abs" role="img" aria-label="Dark desk scene with laptop, tablet and papers"></section>
<section class="member abs" role="img" aria-label="Dark grey keyboard and workspace background"></section>
<div class="divider-diamond abs"></div>
<svg class="abs" style="left:587px;top:668px" width="26" height="22" viewBox="0 0 26 22"><path d="M7 8l6 6 6-6" fill="none" stroke="#1a1a1a" stroke-width="2.5"/></svg>

<h2 class="section-dark-title abs" style="left:80px;top:727px">HOW IT WORKS</h2>
<svg class="abs" style="left:30px;top:790px" width="560" height="450" viewBox="0 0 560 450">
  <path d="M75 90 C140 160 180 190 235 230" fill="none" stroke="#bbb" stroke-width="2" stroke-dasharray="6 6"/>
  <path d="M290 250 C340 270 370 280 405 300" fill="none" stroke="#bbb" stroke-width="2" stroke-dasharray="6 6"/>
  <circle cx="75" cy="90" r="72" fill="#5a5a5a" stroke="#777" stroke-width="2"/>
  <circle cx="75" cy="90" r="55" fill="#3a3a3a"/>
  <path d="M75 62v36M62 86l13 13 13-13" fill="none" stroke="#fff" stroke-width="5"/>
  <path d="M52 100v14h46v-14" fill="none" stroke="#fff" stroke-width="5"/>
  <circle cx="237" cy="245" r="82" fill="#3e88cf" opacity=".55"/>
  <circle cx="237" cy="245" r="66" fill="#1e8ff0" stroke="#fff" stroke-width="2"/>
  <rect x="213" y="221" width="46" height="46" rx="3" fill="none" stroke="#fff" stroke-width="5"/>
  <path d="M221 243l12 13 28-30" fill="none" stroke="#fff" stroke-width="6"/>
  <circle cx="450" cy="305" r="72" fill="#5a5a5a" stroke="#777" stroke-width="2"/>
  <circle cx="450" cy="305" r="55" fill="#3a3a3a"/>
  <ellipse cx="445" cy="285" rx="22" ry="8" fill="#fff"/>
  <rect x="423" y="289" width="44" height="10" fill="#fff"/><rect x="423" y="303" width="44" height="10" fill="#fff"/><rect x="423" y="317" width="30" height="10" fill="#fff"/>
  <circle cx="466" cy="325" r="12" fill="none" stroke="#fff" stroke-width="4"/>
</svg>
<div class="step-title abs" style="left:238px;top:812px">FREE Diagnostic</div>
<div class="step-text abs" style="left:212px;top:843px;width:190px;text-align:right">Get a diagnostic, FOR FREE!<br>Get a free consultation with<br>our staff.</div>
<div class="step-title abs" style="left:333px;top:923px">Backup your information!</div>
<div class="step-text abs" style="left:320px;top:955px;width:220px;text-align:right">Saving your files is now<br>EASY! You will be able to<br>retain your personal files...</div>
<div class="step-title abs" style="left:112px;top:1098px">Get Fixed</div>
<div class="step-text abs" style="left:62px;top:1133px;width:200px;text-align:center">Get fixed, IMMEDIATELY! Our<br>staff will solve your computer<br>issues right before your eyes.</div>

<h2 class="section-dark-title abs" style="left:632px;top:727px">BECOME A &nbsp;MEMBER TODAY</h2>
<div class="abs" role="img" aria-label="Technician working on an open desktop computer tower" style="left:598px;top:790px;width:280px;height:220px;background:linear-gradient(135deg,#6a6a6a,#2e2e2e 60%,#555)"></div>
<div class="abs" style="left:935px;top:822px;font-size:23px;color:var(--white)">Starting At ONLY</div>
<div class="abs" style="left:942px;top:858px;font-size:20px;color:var(--blue)">$</div>
<div class="abs price" style="left:962px;top:852px;font-family:'Lato',sans-serif;font-size:70px;font-weight:300">19.99</div>
<div class="abs" style="left:1050px;top:943px;font-size:19px;color:var(--white)">/ month</div>
<div class="btn" style="left:760px;top:1053px;width:262px;height:50px">Book Now</div>
<div class="abs" style="left:832px;top:1116px;font-size:12.5px;color:#ddd">...or Get help Now:</div>
<div class="abs" style="left:734px;top:1145px;width:312px;height:60px;background:var(--white);border-radius:3px;display:flex;align-items:center;justify-content:center;gap:8px;font-size:15px;color:#555">
  <svg width="16" height="16" viewBox="0 0 24 24"><path d="M6.6 10.8a15 15 0 006.6 6.6l2.2-2.2c.3-.3.7-.4 1-.2 1.1.4 2.3.6 3.6.6.6 0 1 .4 1 1V20c0 .6-.4 1-1 1A17 17 0 013 4c0-.6.4-1 1-1h3.5c.6 0 1 .4 1 1 0 1.3.2 2.5.6 3.6.1.3 0 .7-.2 1z" fill="#1e8ff0"/></svg>
  by Phone : <span style="color:var(--blue);font-size:20px">(888) 555-0142</span>
</div>

<!-- About -->
<h2 class="about-title abs">About US</h2>
<p class="about-text abs" style="top:1355px">Our team is a leader in providing top notch quality services and products with a focus on our customer's needs. We are happy to discuss your computer issues and provide a free valuable diagnostic to determine the best solutions.</p>
<p class="about-text abs" style="top:1442px">While you are looking for the best source out there, we have everything for your computer and internet security!</p>
<div class="btn" style="left:78px;top:1512px;width:144px;height:46px">Read More</div>
<div class="monitor abs" role="img" aria-label="Photo of a desktop monitor showing the company name on its screen"></div>
<div class="quote-band abs"></div>
<div class="about-photo abs" role="img" aria-label="Smiling woman working on a laptop on a white sofa"></div>
<div class="quote-mark abs">“</div>
<p class="quote-text abs">"I contacted them about a serious threat on my laptop, they have completely transformed the laptop, it now functions like a brand new laptop, the staff were excellent, really patient and helpful, excellent service and &nbsp;would highly recommend, thank you."</p>
<div class="quote-name abs">- Martin Hale</div>
<div class="quote-place abs">Uk</div>
<div class="dots abs"><span class="on"></span><span></span><span></span></div>

<!-- Features -->
<h2 class="features-title abs">All the best features, AT THE BEST PRICE!</h2>
<div class="features abs">
  <div class="feature"><div class="feature-ring"><div class="inner">
    <svg width="80" height="64" viewBox="0 0 80 64"><rect x="8" y="22" width="44" height="28" fill="#222"/><path d="M2 52h56l-6 6H8z" fill="#444"/><circle cx="60" cy="16" r="12" fill="none" stroke="#888" stroke-width="2"/><rect x="55" y="14" width="3" height="7" fill="#666"/><rect x="60" y="10" width="3" height="11" fill="#666"/></svg>
  </div></div><div class="feature-name">Regular Tune - Ups</div></div>
  <div class="feature"><div class="feature-ring"><div class="inner">
    <svg width="60" height="72" viewBox="0 0 60 72"><rect x="6" y="4" width="48" height="64" fill="none" stroke="#222" stroke-width="3"/><path d="M22 30a10 10 0 1 0 10-10v10z" fill="#222"/><rect x="36" y="22" width="12" height="3" fill="#222"/><rect x="36" y="30" width="12" height="3" fill="#222"/><rect x="14" y="46" width="32" height="3" fill="#222"/><rect x="14" y="54" width="32" height="3" fill="#222"/></svg>
  </div></div><div class="feature-name">System Report</div></div>
  <div class="feature active"><div class="feature-ring"><div class="inner">
    <svg width="80" height="70" viewBox="0 0 80 70"><rect x="4" y="4" width="72" height="46" fill="none" stroke="#1e8ff0" stroke-width="5"/><path d="M28 16l24 22M52 16L28 38" stroke="#1e8ff0" stroke-width="5"/><path d="M32 50v10M48 50v10M22 62h36" stroke="#1e8ff0" stroke-width="5"/></svg>
  </div></div><div class="feature-name">Ad Blocker</div><div class="feature-more">READ MORE</div></div>
  <div class="feature"><div class="feature-ring"><div class="inner">
    <svg width="80" height="70" viewBox="0 0 80 70"><rect x="6" y="4" width="22" height="36" rx="3" fill="none" stroke="#444" stroke-width="2.5"/><rect x="36" y="30" width="38" height="26" fill="none" stroke="#444" stroke-width="2.5"/><path d="M48 62h14M34 8h30v18M6 48v14h22" fill="none" stroke="#444" stroke-width="2" stroke-dasharray="4 3"/></svg>
  </div></div><div class="feature-name">Cross Platform Support</div></div>
  <div class="feature"><div class="feature-ring"><div class="inner">
    <svg width="84" height="64" viewBox="0 0 84 64"><path d="M22 56H18a14 14 0 0 1 0-28 20 20 0 0 1 38-6 16 16 0 0 1 12 34h-6" fill="none" stroke="#444" stroke-width="5"/><path d="M42 60V32M32 42l10-10 10 10" fill="none" stroke="#444" stroke-width="5"/></svg>
  </div></div><div class="feature-name">Cloud Backup</div></div>
</div>

<!-- Help -->
<section class="help abs" role="img" aria-label="Soft blurred keyboard background"></section>
<h2 class="help-title abs">We are here to help you!</h2>
<p class="help-text abs">Lorem Ipsum is simply dummy text of the printing and typesetting industry. Lorem Ipsum has been the industry's standard dummy text ever since the 1500.</p>
<div class="btn help-btn" style="left:380px;width:218px">Get A Free Quote</div>
<div class="btn help-btn" style="left:604px;width:216px">Get Pricing</div>

<!-- Footer -->
<footer class="footer abs" role="img" aria-label="Dark wooden desk with laptops seen from above"></footer>
<h3 class="footer-head abs" style="left:80px;top:2838px">Useful Links</h3>
<ul class="footer-list abs" style="left:80px;top:2882px"><li>Home</li><li>About us</li><li>Services</li><li>FAQ's</li><li>Contact Us</li></ul>
<h3 class="footer-head abs" style="left:344px;top:2838px">Get in touch</h3>
<svg class="abs" style="left:338px;top:2888px" width="16" height="20" viewBox="0 0 16 20"><path d="M8 0a7 7 0 0 0-7 7c0 5 7 13 7 13s7-8 7-13a7 7 0 0 0-7-7zm0 10a3 3 0 1 1 0-6 3 3 0 0 1 0 6z" fill="#fff"/></svg>
<p class="footer-text abs" style="left:366px;top:2884px;width:220px">Northvale Ltd, 2841 Harbour St. 3rd Floor, Lakeport, NS B0X 2K4 Canada</p>
<svg class="abs" style="left:340px;top:2977px" width="16" height="16" viewBox="0 0 24 24"><path d="M6.6 10.8a15 15 0 006.6 6.6l2.2-2.2c.3-.3.7-.4 1-.2 1.1.4 2.3.6 3.6.6.6 0 1 .4 1 1V20c0 .6-.4 1-1 1A17 17 0 013 4c0-.6.4-1 1-1h3.5c.6 0 1 .4 1 1 0 1.3.2 2.5.6 3.6.1.3 0 .7-.2 1z" fill="#fff"/></svg>
<p class="footer-text abs" style="left:366px;top:2974px">(888) 555-0142</p>
<svg class="abs" style="left:340px;top:3029px" width="18" height="14" viewBox="0 0 18 14"><rect x="1" y="1" width="16" height="12" fill="none" stroke="#fff" stroke-width="1.6"/><path d="M1 1l8 7 8-7" fill="none" stroke="#fff" stroke-width="1.6"/></svg>
<p class="footer-text abs" style="left:366px;top:3025px">info@brightdesk.com</p>
<h3 class="footer-head abs" style="left:606px;top:2838px">NewsLetter</h3>
<p class="footer-text abs" style="left:614px;top:2878px;width:230px;font-size:13.5px;line-height:21px">Lorem Ipsum is simply dummy text of the printing.</p>
<div class="abs" style="left:614px;top:2946px;width:218px;height:46px;border:1px solid #ccc;color:var(--white);font-size:13px;padding:14px 10px">Email</div>
<div class="abs" style="left:614px;top:2998px;width:178px;height:48px;background:var(--white);color:#222;font-size:17px;display:flex;align-items:center;justify-content:center">Submit</div>
<div class="brand footer-brand abs"><span class="dot" style="width:42px;height:42px"></span>brightdesk</div>
<p class="footer-text abs" style="left:900px;top:2900px;width:224px;text-align:right;font-size:13.5px;line-height:20px">We are a group of technicians who work round the clock to ensure that your PC works perfectly. Get your computer free of suspicious software and have a healthy system.</p>
<div class="social abs" style="left:960px;top:3020px;background:var(--blue)"></div>
<div class="social abs" style="left:1024px;top:3020px;background:transparent"></div>
<div class="copyright abs">©&nbsp;<u>Brightdesk</u>&nbsp;- 2017. &nbsp;All Rights Reserved.</div>

</body>
</html>
```